Conservative, Modern and Sharp Builder Business card

Hi there,
We would like to update our existing business card.
I have attached photos of existing business card, logo and van sign.

I would like the business card to also list what we do :
Renovation • New Build • Alteration
Extension • Bathroom • Maintenance.(Seperated by dots)

Contact number : 021 0483 0752
(With that exact spacing)

Ideally when people looking from about 2-3 metres, they know that it is a builder’s business card

Open to suggestions on fonts, layout, style of business card

PLEASE ONLY SUBMIT YOUR BEST OR MAX 3 DESIGNS FOR EACH DESIGNER

Thanks

Construction. Renovation

Details should be the same as the existing card. And addition of what we do.

• The new business card must not have the same layout as our existing one. Thanks

```html
<!DOCTYPE html>
<html lang="en">
<head>
<meta charset="utf-8">
<title>KestrelBuild Business Card</title>
<link href="https://fonts.googleapis.com/css2?family=Lato:wght@400;700;900&display=swap" rel="stylesheet">
<style>
  :root {
    --ink: #0d0d0d;
    --paper: #ffffff;
    --stage: #2a2a2a;
    --rule: #1a1a1a;
  }
  * { box-sizing: border-box; margin: 0; padding: 0; }
  html, body {
    width: 1200px; height: 900px; overflow: hidden;
    background: var(--stage);
    font-family: "Lato", sans-serif;
  }
  .canvas { position: relative; width: 1200px; height: 900px; }
  .card {
    position: absolute; left: 260px;
    width: 680px; height: 389px;
    border-radius: 22px; overflow: hidden;
  }
  /* Front */
  .card-front { top: 36px; background: var(--ink); color: var(--paper); }
  .brand {
    position: absolute; left: 0; right: 0; top: 120px;
    display: flex; align-items: center; justify-content: center; gap: 16px;
  }
  .brand-square { width: 26px; height: 26px; background: var(--paper); }
  .brand-name { font-weight: 900; font-size: 86px; letter-spacing: -1px; line-height: 1; }
  .services {
    position: absolute; left: 0; right: 0; bottom: 58px;
    text-align: center; font-size: 19px; font-weight: 400; letter-spacing: 0.3px;
  }
  /* Back */
  .card-back { top: 475px; background: var(--paper); }
  .back-inner {
    position: absolute; width: 389px; height: 680px;
    left: 145.5px; top: -145.5px;
    transform: rotate(-90deg);
    color: var(--ink);
  }
  .back-panel { position: absolute; left: 0; top: 0; width: 389px; height: 300px; }
  .person { position: absolute; left: 0; right: 0; top: 318px; text-align: center; }
  .person-name { font-weight: 900; font-size: 34px; letter-spacing: 0.5px; text-transform: uppercase; }
  .person-role { font-size: 19px; margin-top: 4px; }
  .icon-row {
    position: absolute; left: 30px; right: 30px; top: 410px;
    display: flex; align-items: center; gap: 14px;
  }
  .icon-row .rule { flex: 1; height: 2px; background: var(--rule); }
  .icon { width: 36px; height: 36px; border-radius: 50%; background: var(--ink); display: flex; align-items: center; justify-content: center; }
  .contact { position: absolute; left: 0; right: 0; top: 468px; text-align: center; line-height: 1.3; }
  .contact-phone { font-weight: 700; font-size: 30px; letter-spacing: 1px; }
  .contact-line { font-size: 19px; }
  .divider { position: absolute; left: 30px; right: 30px; top: 585px; height: 2px; background: var(--rule); }
  .social {
    position: absolute; left: 0; right: 0; top: 610px;
    display: flex; justify-content: center; align-items: center; gap: 8px;
    font-size: 19px;
  }
  .social-dot { width: 16px; height: 16px; border-radius: 50%; border: 2px solid var(--ink); }
</style>
</head>
<body>
<div class="canvas">
  <section class="card card-front">
    <div class="brand">
      <span class="brand-square"></span>
      <span class="brand-name">KestrelBuild</span>
    </div>
    <p class="services">Renovation • New Build • Alteration • Extension • Bathroom • Maintenance</p>
  </section>

  <section class="card card-back">
    <div class="back-inner">
      <svg class="back-panel" viewBox="0 0 389 300" aria-hidden="true">
        <polygon points="0,0 389,0 389,300 0,235" fill="var(--ink)"/>
        <rect x="150" y="95" width="34" height="34" fill="var(--paper)"/>
      </svg>
      <div class="person">
        <p class="person-name">Maren Tollis</p>
        <p class="person-role">Residential Builder</p>
      </div>
      <div class="icon-row">
        <span class="rule"></span>
        <span class="icon">
          <svg width="18" height="18" viewBox="0 0 24 24"><path d="M6.6 10.8a15 15 0 0 0 6.6 6.6l2.2-2.2a1 1 0 0 1 1-.25 11.4 11.4 0 0 0 3.6.57 1 1 0 0 1 1 1V20a1 1 0 0 1-1 1A17 17 0 0 1 3 4a1 1 0 0 1 1-1h3.5a1 1 0 0 1 1 1c0 1.25.2 2.45.57 3.57a1 1 0 0 1-.25 1z" fill="#fff"/></svg>
        </span>
        <span class="icon">
          <svg width="18" height="18" viewBox="0 0 24 24"><rect x="3" y="6" width="18" height="12" fill="none" stroke="#fff" stroke-width="2"/><path d="M3 6l9 7 9-7" fill="none" stroke="#fff" stroke-width="2"/></svg>
        </span>
        <span class="icon">
          <svg width="18" height="18" viewBox="0 0 24 24"><circle cx="12" cy="12" r="9" fill="none" stroke="#fff" stroke-width="2"/><ellipse cx="12" cy="12" rx="4" ry="9" fill="none" stroke="#fff" stroke-width="1.6"/><path d="M3 12h18" stroke="#fff" stroke-width="1.6"/></svg>
        </span>
        <span class="rule"></span>
      </div>
      <div class="contact">
        <p class="contact-phone">021 0483 0752</p>
        <p class="contact-line">KestrelBuild@mailbox.co.nz</p>
        <p class="contact-line">www.KestrelBuild.nz</p>
      </div>
      <div class="divider"></div>
      <div class="social">
        <span class="social-dot"></span>
        <span>KestrelBuild.nz</span>
      </div>
    </div>
  </section>
</div>
</body>
</html>
```